Chiropractic healthcare group business card

We are a Portland Oregon based chiropractic healthcare group. Looking for a new business card design. Something cutting edge, that shows off our new logo and tag line.Use either of the attached logos.Our tag line = "Who would you be without pain?"I'm open to about anything, impress me!!
Target Market(s)
Chiropractic patients - Auto injury, back pain, sports injuries, neck , shoulder, hip, knee, ankle pain.
Industry/Entity Type
Chiropractic
Contact Information for Business Card
Dr. Bram Holtvick, D.C.
Clinic name - Fernway Chiropractic
2 clinics
location #1
20418 NW Marwick Road
Suite B
North Plains, OR 97133
Location #2
13529 SE Calloway Street
Portland OR 97236
Main phone line 971.555.0143
website : www.FernwayClinics.example
Tag line "Who would you be without pain?"
Colors
Designer to choose colors to be used in the design.
Requirements
Must have
- Use the logo colors -- Want the orange color to be a TRUE orange.
- Both clinic address
- phone number
- website
- personal email - b.holtvick@ReliefBeginsHere.example
- tag line - "Who would you be without pain?"

```html
<!DOCTYPE html>
<html lang="en">
<head>
<meta charset="utf-8">
<title>Fernway Chiropractic – Business Card</title>
<link rel="stylesheet" href="https://fonts.googleapis.com/css2?family=Alegreya:wght@400;700&family=Dancing+Script:wght@600&display=swap">
<style>
  :root {
    --stage: #eceeef;
    --card-white: #ffffff;
    --slate: #4d4d4d;
    --ink: #1f1f1f;
    --true-orange: #f7931e;
    --salmon: #f2834f;
    --band-start: #ff9545;
    --band-end: #ffd44f;
    --serif: "Alegreya", Georgia, serif;
    --script: "Dancing Script", cursive;
  }
  * { box-sizing: border-box; margin: 0; padding: 0; }
  html, body { width: 1200px; height: 806px; overflow: hidden; }
  body {
    background: var(--stage);
    font-family: var(--serif);
    position: relative;
  }
  .card {
    position: absolute;
    top: 217px;
    width: 540px;
    height: 372px;
    background: var(--card-white);
    overflow: hidden;
    box-shadow: 0 6px 18px rgba(0,0,0,.12);
  }
  .card--front { left: 40px; }
  .card--back { left: 620px; }

  .front__panel { position: absolute; inset: 0; }

  .brand {
    position: absolute;
    display: flex;
    align-items: center;
    gap: 8px;
    font-family: var(--serif);
    font-weight: 700;
    color: var(--slate);
    letter-spacing: .08em;
    text-transform: uppercase;
    line-height: 1.05;
  }
  .brand__mark { width: 16px; height: 16px; background: var(--true-orange); flex: none; }
  .card--front .brand { top: 54px; right: 26px; font-size: 19px; text-align: left; }
  .card--back .brand { top: 70px; left: 205px; font-size: 22px; }

  .front__clinic {
    position: absolute; left: 52px; top: 146px;
    color: #fff; font-size: 22px; font-weight: 400; letter-spacing: .02em;
    white-space: nowrap;
  }
  .front__doctor {
    position: absolute; left: 52px; top: 200px;
    color: var(--true-orange); font-size: 25px; font-weight: 700;
    white-space: nowrap;
  }
  .front__contact {
    position: absolute; left: 52px; top: 262px;
    color: #fff; font-size: 15.5px; line-height: 1.6; list-style: none;
  }

  .office { position: absolute; font-size: 17px; line-height: 1.5; color: var(--ink); font-style: normal; }
  .office__title { color: var(--salmon); font-size: 18px; font-weight: 400; }
  .office--north { left: 318px; top: 150px; }
  .office--portland { left: 36px; top: 200px; }

  .tagline-band {
    position: absolute; left: 0; right: 0; bottom: 0; height: 74px;
    background: linear-gradient(90deg, var(--band-start), var(--band-end));
    display: flex; align-items: center; justify-content: center;
  }
  .tagline {
    font-family: var(--script); font-size: 27px; color: var(--ink);
  }
</style>
</head>
<body>
  <section class="card card--front" aria-label="Business card front">
    <svg class="front__panel" viewBox="0 0 540 372" width="540" height="372" aria-hidden="true">
      <polygon points="0,0 227,0 540,372 0,372" fill="var(--slate)"/>
    </svg>
    <div class="brand"><span class="brand__mark"></span><span>Fernway<br>Chiropractic</span></div>
    <h1 class="front__clinic">FERNWAY CHIROPRACTIC</h1>
    <h2 class="front__doctor">DR. BRAM HOLTVICK, D.C.</h2>
    <ul class="front__contact">
      <li>Phone: 971.555.0143</li>
      <li>Email: b.holtvick@ReliefBeginsHere.example</li>
      <li>Website: www.FernwayClinics.example</li>
    </ul>
  </section>

  <section class="card card--back" aria-label="Business card back">
    <div class="brand"><span class="brand__mark"></span><span>Fernway<br>Chiropractic</span></div>
    <address class="office office--north">
      <h3 class="office__title">North Plains Office</h3>
      20418 NW Marwick Road<br>Suite B<br>North Plains, OR 97133
    </address>
    <address class="office office--portland">
      <h3 class="office__title">Portland Office</h3>
      13529 SE Calloway Street<br>Portland OR 97236
    </address>
    <div class="tagline-band"><p class="tagline">Who would you be without pain?</p></div>
  </section>
</body>
</html>
```